Natural Skincare brand needs new labels!

We are a natural and organic skin care brand based in the united states. We are looking for unique product label designs that will help our brand stand out. We want the labels to look elegant and natural, but also incorporate some color. We want a design aspect like a line drawing on the labels, see examples. Please refer to our website to see our current labels and to get more of a feel of who we are. Our logo is included. We are looking for 5 labels for 5 different Products.
1. Body butter: 1.5"x9" rectangle wrap around 12oz jar with black lid
2. Eczema Salve: 1.5" circle silver metal tin
3. Glow Serum: 1.5"x3" rectangle Blue Dropper Bottle with black top
4. Mineral Mist: 1.5"x3" clear glass sprayer bottle (want clear label)
website: www.velmirabotanics.com
Instagram: @velmirabotanics

```html
<!DOCTYPE html>
<html lang="en">
<head>
<meta charset="utf-8">
<title>Velmira Botanics – Body Butter and Eczema Salve Labels</title>
<link rel="stylesheet" href="https://fonts.googleapis.com/css2?family=Poppins:ital,wght@0,400;0,500;0,600;0,700;1,600&display=swap">
<style>
  :root {
    --page: #ffffff;
    --label-bg: #efeeef;
    --lavender: #9a88c6;
    --coral: #f07a6c;
    --ink: #2b2b2b;
    --ink-soft: #4a4a4a;
    --sketch: #d9d6dc;
    --dash: #6d6d6d;
    --white: #ffffff;
  }
  * { box-sizing: border-box; margin: 0; padding: 0; }
  html, body {
    width: 914px; height: 1200px; overflow: hidden;
    background: var(--page);
    font-family: "Poppins", sans-serif;
    color: var(--ink);
  }
  .canvas { position: relative; width: 914px; height: 1200px; }

  /* ---------- Wrap-around body butter label ---------- */
  .wrap-label {
    position: absolute; left: 47px; top: 380px;
    width: 820px; height: 135px;
    background: var(--label-bg);
    box-shadow: 2px 3px 5px rgba(0,0,0,0.25);
    overflow: hidden;
  }
  .wrap-label .top-edge { position: absolute; left: 0; top: 0; width: 820px; height: 9px; }
  .wrap-label .bottom-rule {
    position: absolute; left: 0; bottom: 0; width: 100%; height: 2px; background: var(--coral);
  }
  .fine-print {
    position: absolute; font-size: 4.4px; line-height: 5.5px;
    text-align: justify; color: var(--ink-soft);
  }
  .fine-print b { color: var(--ink); font-weight: 700; }
  .ingredients-text { left: 24px; top: 26px; width: 223px; }
  .how-to-text { left: 571px; top: 26px; width: 223px; }
  .benefit-text { left: 571px; top: 72px; width: 223px; }
  .caution-box {
    position: absolute; left: 25px; top: 78px; width: 222px; height: 36px;
    border: 1px dashed var(--dash); border-radius: 16px;
    padding: 4px 10px;
    font-size: 5px; line-height: 6px; font-style: italic; font-weight: 600;
    color: var(--coral); text-align: justify;
  }
  .sprig-art {
    position: absolute; left: 290px; top: 6px; width: 113px; height: 108px;
    background: radial-gradient(ellipse at 50% 50%, #cfcbd2 0%, var(--label-bg) 72%);
    border-radius: 40%;
  }
  .brand-mark { position: absolute; display: flex; align-items: center; gap: 4px; }
  .brand-mark .dot { border-radius: 50%; background: var(--coral); flex: none; }
  .brand-name { color: var(--coral); font-weight: 500; white-space: nowrap; }
  .wrap-label .brand-mark { left: 424px; top: 30px; }
  .wrap-label .dot { width: 9px; height: 9px; }
  .wrap-label .brand-name { font-size: 10.5px; }
  .product-title {
    position: absolute; left: 422px; top: 65px;
    font-size: 14.5px; font-weight: 400; letter-spacing: -0.2px; line-height: 1;
  }
  .product-title .accent { color: var(--coral); }
  .scent-bar {
    position: absolute; left: 423px; top: 86px; width: 92px; height: 11px;
    background: var(--lavender); color: var(--white);
    font-size: 6.5px; letter-spacing: 3.2px; text-align: center; line-height: 11px;
  }
  .benefits {
    position: absolute; left: 423px; top: 103px; width: 100px;
    font-size: 5px; line-height: 7px; color: var(--ink-soft);
  }
  .size-tab {
    position: absolute; left: 497px; bottom: 0; width: 21px; height: 15px;
    background: var(--coral); color: var(--white);
    border-radius: 11px 11px 0 0;
    font-size: 5.5px; text-align: center; line-height: 17px;
  }
  .natural-pill {
    position: absolute; left: 573px; top: 102px; width: 149px; height: 17px;
    background: var(--coral); color: var(--white); border-radius: 9px;
    font-size: 7.6px; font-weight: 600; line-height: 17px; padding-left: 7px;
  }

  /* ---------- Round eczema salve lid label ---------- */
  .lid-label {
    position: absolute; left: 287px; top: 595px;
    width: 340px; height: 340px; border-radius: 50%;
    background: var(--label-bg);
    border: 8px solid var(--lavender);
    overflow: hidden;
  }
  .lid-inner { position: absolute; left: -8px; top: -8px; width: 340px; height: 340px; }
  .lid-label .brand-mark { left: 52px; top: 52px; flex-direction: column; align-items: flex-start; gap: 2px; }
  .lid-label .dot { width: 16px; height: 16px; margin-left: 98px; }
  .lid-label .brand-name { font-size: 25px; line-height: 1.05; }
  .salve-title {
    position: absolute; left: 52px; top: 173px;
    font-size: 20px; font-weight: 500; letter-spacing: -0.3px; line-height: 1;
  }
  .salve-claim {
    position: absolute; left: 53px; top: 195px; height: 15px;
    background: var(--coral); color: var(--white);
    font-size: 9px; font-weight: 500; padding: 0 4px; line-height: 15px;
  }
  .salve-note {
    position: absolute; left: 53px; top: 216px;
    font-size: 8.2px; color: var(--ink-soft);
  }
  .salve-ingredients {
    position: absolute; left: 53px; top: 237px; width: 150px;
    font-size: 8.8px; line-height: 11.5px; color: var(--ink-soft);
  }
  .salve-weight {
    position: absolute; left: 122px; top: 302px;
    font-size: 13px; color: var(--ink);
  }
  .salve-size-tab {
    position: absolute; left: 158px; top: 299px; width: 36px; height: 45px;
    background: var(--lavender); color: var(--white);
    border-radius: 14px 14px 0 0;
    font-size: 12px; text-align: center; padding-top: 4px;
  }
  .salve-size-tab sup { font-size: 7px; }
  .flower-art {
    position: absolute; left: 208px; top: 120px; width: 112px; height: 190px;
    background: radial-gradient(ellipse at 50% 45%, #cdc9d0 0%, var(--label-bg) 70%);
    border-radius: 45%;
  }
</style>
</head>
<body>
<main class="canvas">

  <section class="wrap-label" aria-label="Body butter wrap-around label">
    <svg class="top-edge" viewBox="0 0 820 9" preserveAspectRatio="none" aria-hidden="true">
      <rect x="0" y="0" width="820" height="4" fill="var(--lavender)"/>
      <path fill="var(--lavender)" d="M0 4 q2.5 4 5 0 q2.5 4 5 0 q2.5 4 5 0 q2.5 4 5 0 q2.5 4 5 0 q2.5 4 5 0 q2.5 4 5 0 q2.5 4 5 0 q2.5 4 5 0 q2.5 4 5 0 q2.5 4 5 0 q2.5 4 5 0 q2.5 4 5 0 q2.5 4 5 0 q2.5 4 5 0 q2.5 4 5 0 q2.5 4 5 0 q2.5 4 5 0 q2.5 4 5 0 q2.5 4 5 0 q2.5 4 5 0 q2.5 4 5 0 q2.5 4 5 0 q2.5 4 5 0 q2.5 4 5 0 q2.5 4 5 0 q2.5 4 5 0 q2.5 4 5 0 q2.5 4 5 0 q2.5 4 5 0 q2.5 4 5 0 q2.5 4 5 0 q2.5 4 5 0 q2.5 4 5 0 q2.5 4 5 0 q2.5 4 5 0 q2.5 4 5 0 q2.5 4 5 0 q2.5 4 5 0 q2.5 4 5 0 q2.5 4 5 0 q2.5 4 5 0 q2.5 4 5 0 q2.5 4 5 0 q2.5 4 5 0 q2.5 4 5 0 q2.5 4 5 0 q2.5 4 5 0 q2.5 4 5 0 q2.5 4 5 0 q2.5 4 5 0 q2.5 4 5 0 q2.5 4 5 0 q2.5 4 5 0 q2.5 4 5 0 q2.5 4 5 0 q2.5 4 5 0 q2.5 4 5 0 q2.5 4 5 0 q2.5 4 5 0 q2.5 4 5 0 q2.5 4 5 0 q2.5 4 5 0 q2.5 4 5 0 q2.5 4 5 0 q2.5 4 5 0 q2.5 4 5 0 q2.5 4 5 0 q2.5 4 5 0 q2.5 4 5 0 q2.5 4 5 0 q2.5 4 5 0 q2.5 4 5 0 q2.5 4 5 0 q2.5 4 5 0 q2.5 4 5 0 q2.5 4 5 0 q2.5 4 5 0 q2.5 4 5 0 q2.5 4 5 0 q2.5 4 5 0 q2.5 4 5 0 q2.5 4 5 0 q2.5 4 5 0 q2.5 4 5 0 q2.5 4 5 0 q2.5 4 5 0 q2.5 4 5 0 q2.5 4 5 0 q2.5 4 5 0 q2.5 4 5 0 q2.5 4 5 0 q2.5 4 5 0 q2.5 4 5 0 q2.5 4 5 0 q2.5 4 5 0 q2.5 4 5 0 q2.5 4 5 0 q2.5 4 5 0 q2.5 4 5 0 q2.5 4 5 0 q2.5 4 5 0 q2.5 4 5 0 q2.5 4 5 0 q2.5 4 5 0 q2.5 4 5 0 q2.5 4 5 0 q2.5 4 5 0 q2.5 4 5 0 q2.5 4 5 0 q2.5 4 5 0 q2.5 4 5 0 q2.5 4 5 0 q2.5 4 5 0 q2.5 4 5 0 q2.5 4 5 0 q2.5 4 5 0 q2.5 4 5 0 q2.5 4 5 0 q2.5 4 5 0 q2.5 4 5 0 q2.5 4 5 0 q2.5 4 5 0 q2.5 4 5 0 q2.5 4 5 0 q2.5 4 5 0 q2.5 4 5 0 q2.5 4 5 0 q2.5 4 5 0 q2.5 4 5 0 q2.5 4 5 0 q2.5 4 5 0 q2.5 4 5 0 q2.5 4 5 0 q2.5 4 5 0 q2.5 4 5 0 q2.5 4 5 0 q2.5 4 5 0 q2.5 4 5 0 q2.5 4 5 0 q2.5 4 5 0 q2.5 4 5 0 q2.5 4 5 0 q2.5 4 5 0 q2.5 4 5 0 q2.5 4 5 0 q2.5 4 5 0 q2.5 4 5 0 q2.5 4 5 0 L820 4 Z"/>
    </svg>

    <p class="fine-print ingredients-text"><b>Ingredients</b> Whipped shea butter, cocoa butter, virgin coconut oil, sweet almond oil, jojoba oil, lavender essential oil, vitamin E oil and a touch of arrowroot powder. Every batch is made by hand in small runs, using plant based butters and oils that are sourced from trusted growers. No parabens, no synthetic fragrance, no dyes, no fillers. Store in a cool dry place away from direct sunlight and keep the lid closed tight.</p>

    <p class="caution-box">For external use only. Patch test before first use and stop use if irritation occurs. Keep out of reach of children. Not tested on animals.</p>

    <div class="sprig-art" role="img" aria-label="Line drawing of a leafy lavender sprig"></div>

    <div class="brand-mark">
      <span class="dot"></span>
      <span class="brand-name">Velmira Botanics</span>
    </div>
    <h1 class="product-title">BODY <span class="accent">BUTTER</span></h1>
    <div class="scent-bar">LAVENDER</div>
    <p class="benefits">Moisturizing+Nourishing+Sensitive<br>Dry Skin</p>
    <div class="size-tab">12<sup>oz</sup></div>

    <p class="fine-print how-to-text"><b>How to use</b> Scoop a small amount with clean dry fingers and warm it between your palms. Massage into damp skin after a bath or shower, paying extra attention to elbows, knees and heels. Use morning and night, or whenever skin feels tight and dry. A little goes a long way, so start small and add more as needed.</p>

    <p class="fine-print benefit-text">Lavender calms the senses while rich butters melt in to soften and protect. Made for sensitive and very dry skin, this blend leaves a soft finish without a greasy feel. Handmade in small batches in the United States.</p>

    <div class="natural-pill">Made With all natural ingredients</div>
    <div class="bottom-rule"></div>
  </section>

  <section class="lid-label" aria-label="Eczema salve round lid label">
    <div class="lid-inner">
      <div class="brand-mark">
        <span class="dot"></span>
        <span class="brand-name">Velmira<br>Botanics</span>
      </div>
      <h2 class="salve-title">ECZEMA SALVE</h2>
      <div class="salve-claim">HEALING &amp; REGENERATING</div>
      <p class="salve-note">Made With all natural ingredients</p>
      <p class="salve-ingredients">sesame oil^, calendula flowers^, licorice root^, plantain leaf^, vitamin E oil^, beeswax^</p>
      <div class="salve-weight">29g</div>
      <div class="salve-size-tab">1<sup>oz</sup></div>
      <div class="flower-art" role="img" aria-label="Line drawing of a tall wildflower with long leaves"></div>
    </div>
  </section>

</main>
</body>
</html>
```